Premium stylish simple clever card design for high end construction company.

I need a business card designed that is a standard size and shape (square edges) that is black in colour, with black edges. All text is to be either grey/silver or yellow/gold. On the front I want the logo (supplied as attachment g5) to be embossed or raised to give a texture. I also want the name of my company "The Quiet Ember (larger font) construction co. (smaller font)" I like the clean style (found in attachment 56419286) of the black background with silver text. But the triangle is to be gold/yellow.

On the back needs to have my contact details. In silver or gold text.

Marcus Delby - Builder
Marcus@thequietember.com.au
www.thequietember.com.au
0438201965
Lic 517904k
PO BOX 758 Ashcombe NSW 2188

Must look simple, elegant and precise.

My work is of the utmost quality and my business card needs to project that. It needs to be simple and precise. It should scream luxury and confidence. Feel free to get creative with the font and font size. If you google "The Quiet Ember" you will see it has links to great architecture, art, nature and the fibonacci sequence so i am open to using these ideas also.

Target Market(s)

High End home owners. 30-70 year olds.

Industry/Entity Type

Residential Construction

Contact Information for Business Card

Logo and company name on front. Contact details on back.

Font styles to use
Serif
Sans Serif

Colors
ffcf3e

Requirements
Must have
• black background
Nice to have
• debossed logo (silver and gold)
• debased company name (silver)
Should not have
• It should not look like a standard construction business card with pictures of hammers or tools etc.

```html
<!DOCTYPE html>
<html lang="en">
<head>
<meta charset="utf-8">
<title>The Quiet Ember – Business Card</title>
<link rel="stylesheet" href="https://fonts.googleapis.com/css2?family=Lato:wght@300;400;700&display=swap">
<style>
  :root {
    --backdrop: #8a8a8a;
    --card-black: #1f1f1f;
    --card-glow: #3a3a3a;
    --gold: #ffcf3e;
    --silver: #a9a9a9;
    --silver-light: #d6d6d6;
    --white: #ffffff;
    --muted: #9a9a9a;
  }
  * { box-sizing: border-box; margin: 0; padding: 0; }
  html, body {
    width: 1200px; height: 926px; overflow: hidden;
    background: var(--backdrop);
    font-family: "Lato", sans-serif;
  }
  .sheet {
    width: 1200px; height: 926px;
    display: flex; flex-direction: column;
    align-items: center; justify-content: center; gap: 56px;
  }
  .card {
    position: relative;
    width: 620px; height: 379px;
    background: radial-gradient(ellipse at 50% 45%, var(--card-glow) 0%, var(--card-black) 62%);
    overflow: hidden;
    box-shadow: 0 10px 28px rgba(0,0,0,0.35);
  }

  /* Front */
  .tab {
    position: absolute; width: 30px; height: 112px;
    background: var(--gold);
  }
  .tab::after {
    content: ""; position: absolute; top: 0; width: 7px; height: 100%;
    background: var(--white);
  }
  .tab--left { left: 0; top: 58px; }
  .tab--left::after { right: -7px; }
  .tab--right { right: 0; top: 206px; }
  .tab--right::after { left: -7px; }

  .brand {
    position: absolute; left: 0; right: 0; top: 118px;
    display: flex; flex-direction: column; align-items: center;
  }
  .brand__mark {
    width: 62px; height: 62px; border-radius: 50%;
    border: 7px solid var(--silver);
    margin-bottom: 16px;
  }
  .brand__name {
    font-size: 34px; font-weight: 300; letter-spacing: 1px;
    color: var(--silver); text-transform: uppercase;
    padding: 0 6px 2px;
    border-bottom: 1px solid var(--silver);
  }
  .brand__tag {
    font-size: 10px; font-weight: 400; letter-spacing: 1px;
    color: var(--silver); text-transform: uppercase;
    margin-top: 3px;
  }

  /* Back */
  .band {
    position: absolute; left: 0; right: 0; height: 8px;
    background: var(--gold);
  }
  .band--top { top: 0; }
  .band--bottom { bottom: 0; }

  .contact {
    position: absolute; left: 0; right: 0; top: 66px;
    text-align: center;
  }
  .contact__name {
    display: inline-block;
    font-size: 30px; font-weight: 400; color: var(--white);
    text-transform: uppercase; letter-spacing: 0.5px;
    padding: 0 8px 3px;
    border-bottom: 2px solid var(--gold);
  }
  .contact__name strong { font-weight: 700; }
  .contact__role {
    font-size: 14px; font-weight: 700; letter-spacing: 4px;
    color: var(--muted); text-transform: uppercase;
    margin-top: 6px;
  }
  .contact__list {
    list-style: none; margin-top: 22px;
    font-size: 17px; line-height: 26px; color: var(--silver-light);
  }
  .contact__label { color: var(--gold); font-weight: 700; }
  .contact__address { color: var(--muted); margin-top: 6px; }
</style>
</head>
<body>
  <main class="sheet">
    <section class="card card--front" aria-label="Card front">
      <span class="tab tab--left"></span>
      <span class="tab tab--right"></span>
      <div class="brand">
        <span class="brand__mark"></span>
        <h1 class="brand__name">The Quiet Ember</h1>
        <p class="brand__tag">Construction Co.</p>
      </div>
    </section>

    <section class="card card--back" aria-label="Card back">
      <span class="band band--top"></span>
      <span class="band band--bottom"></span>
      <div class="contact">
        <h2 class="contact__name">Marcus <strong>Delby</strong></h2>
        <p class="contact__role">Builder</p>
        <ul class="contact__list">
          <li><span class="contact__label">email-</span> Marcus@thequietember.com.au</li>
          <li><span class="contact__label">web-</span> www.thequietember.com.au</li>
          <li><span class="contact__label">phone-</span> 0438201965</li>
          <li><span class="contact__label">lic-</span> 517904k</li>
        </ul>
        <p class="contact__list contact__address">PO BOX 758 Ashcombe NSW 2188</p>
      </div>
    </section>
  </main>
</body>
</html>
```